Tess Vallory - health and fitness coach who needs a web page. simple and effective

I am a online health and fitness coach who runs a 10 week challenge 4 times a year. I am wanting, a menu with a bit about me, a place where people can buy the programme, testimonies, memberships, photos, and recipes.
I am wanting it to look modern, professional and simple.
The website is how potential clients can check out the memberships for the programme, photos of myself and and my family to show members that I am a confident, educated, independent and healthy woman. Who is very passionate about making a difference in people lives to become a better version of themselves.
My training philosophy is simple, Commitment to training, Consistently working hard and training equals Change! Change is physical changes to the body!!

Target Market(s)

Woman 25-44 years

Industry/Entity Type

Health And Wellness

Coding

Coded - Design and coding required

Number of Pages Required

5+ page

Font styles to use
Sans Serif

Colors
fbed22
e667a6
ffffff

Requirements
Must have
• I like the style of "brick nest" website design.
• On the menu bar I want 9 different tabs/options to click on, these are named:
• BLOG
• ABOUT
• TRAINING PROGRAMS
• HEALTHY FOOD
• SUBSCRIBE
• TESTIMONIALS
• PALSHARE
• SNAPLORIA
• VID HOLLOW
Nice to have
• logo at the top (attached under file 2)
• Easy for myself to add information once website design is completed.
• lots of white space, white a bright yellow (same as logo) or pink
Should not have
• clutter

```html
<!DOCTYPE html>
<html lang="en">
<head>
<meta charset="utf-8">
<title>Tess Vallory – Online Health and Fitness Coach</title>
<link href="https://fonts.googleapis.com/css2?family=Montserrat:wght@400;600;700;800&family=Open+Sans:wght@400;600;700&display=swap" rel="stylesheet">
<style>
:root{
  --yellow:#f4cf1d;
  --yellow-bright:#fbed22;
  --pink:#e14b8a;
  --white:#ffffff;
  --ink:#222222;
  --text:#555555;
  --muted:#8a8a8a;
  --soft:#f2f0f2;
  --line:#e4e2e4;
  --card-dark:#4b4b4b;
  --card-darker:#3a3a3a;
  --ribbon:#5cb85c;
}
*{box-sizing:border-box;margin:0;padding:0}
html,body{width:1200px;height:5028px;overflow:hidden;background:var(--white)}
body{position:relative;font-family:"Open Sans",Arial,sans-serif;color:var(--text)}
.abs{position:absolute}
.section{position:absolute;left:0;width:1200px}

/* header */
.site-header{top:0;height:100px;background:var(--white)}
.brand{display:flex;align-items:center;gap:10px}
.brand-dot{width:14px;height:14px;border-radius:50%;background:var(--pink)}
.brand-name{font-family:"Montserrat",sans-serif;font-weight:700;color:var(--ink);font-size:22px;line-height:26px;white-space:nowrap}
.site-header .brand{left:33px;top:34px}
.follow{right:330px;top:32px;display:flex;align-items:center;gap:7px;font-family:"Montserrat",sans-serif;font-size:9px;font-weight:700;color:var(--ink)}
.follow i{display:block;width:17px;height:17px;border-radius:50%;background:var(--pink)}
.follow i:last-child{background:var(--card-dark)}
.call{right:80px;top:26px;display:flex;align-items:center;gap:10px}
.call-label{font-family:"Montserrat",sans-serif;font-size:9px;font-weight:700;color:var(--ink);line-height:13px}
.call-label b{display:block;font-size:13px;color:var(--ink)}
.main-nav{right:80px;top:82px;display:flex;gap:24px;font-family:"Montserrat",sans-serif;font-size:11px;font-weight:700;color:var(--ink);letter-spacing:.3px}
.main-nav .current{color:var(--pink)}

/* hero */
.hero{top:100px;height:570px;background:linear-gradient(180deg,#f6f3f5,#efe9ed)}
.hero-photo{left:184px;top:117px;width:420px;height:603px;background:linear-gradient(160deg,#fbf36a 0%,#e9e6ea 30%,#6f9fd6 70%,#3d74c0 100%);border-radius:4px}
.hero-copy{position:absolute;left:677px;top:236px;font-family:"Montserrat",sans-serif;color:var(--ink);font-size:40px;line-height:58px;font-weight:400}
.hero-copy strong{font-weight:700;color:var(--yellow)}
.hero-copy .strong-dark{font-weight:700;color:var(--ink)}
.btn{display:inline-flex;align-items:center;gap:8px;background:var(--pink);color:var(--white);font-family:"Montserrat",sans-serif;font-weight:700;font-size:12px;border-radius:3px;padding:0 16px;height:34px}
.hero .btn{position:absolute;left:677px;top:400px;height:46px;font-size:15px;padding:0 22px}
.dots{display:flex;gap:8px}
.dots i{display:block;width:8px;height:8px;border-radius:50%;background:#c7c3c6}
.dots i.on{background:var(--pink)}
.hero .dots{position:absolute;left:1020px;top:515px}

/* section badge */
.badge{position:absolute;left:50%;transform:translateX(-50%);background:var(--yellow);color:var(--white);font-family:"Montserrat",sans-serif;font-weight:800;font-size:20px;letter-spacing:3px;padding:0 26px;height:52px;line-height:52px;text-transform:uppercase;white-space:nowrap}

/* programs */
.programs{top:670px;height:870px}
.program-card{position:absolute;top:275px;width:342px}
.program-photo{height:362px}
.program-title{margin-top:30px;font-family:"Montserrat",sans-serif;font-weight:700;font-size:13px;color:var(--ink);white-space:nowrap}
.program-desc{margin-top:6px;font-size:11px;color:var(--muted);white-space:nowrap}
.program-card .btn{margin-top:24px;height:26px;font-size:11px;padding:0 12px}

/* about */
.about{top:1540px;height:600px}
.about-back{left:94px;top:29px;width:370px;height:476px;background:linear-gradient(150deg,#1d2340,#0b0d18 60%,#2b1c2a)}
.about-photo{left:134px;top:89px;width:563px;height:355px;border:6px solid var(--white);box-shadow:0 10px 30px rgba(0,0,0,.25);background:linear-gradient(120deg,#c9a57a,#e7d2b6 40%,#8a2d2f 75%,#3b2a26)}
.text-block{position:absolute;width:330px}
.text-block .badge{position:static;transform:none;display:inline-block;font-size:17px;height:44px;line-height:44px;padding:0 20px}
.text-block h3{margin-top:26px;font-family:"Montserrat",sans-serif;font-weight:700;font-size:17px;line-height:24px;color:var(--ink)}
.text-block p{margin-top:12px;font-size:11px;line-height:18px;color:var(--muted)}
.text-block .btn{margin-top:26px;height:28px;font-size:11px}
.about .text-block{left:771px;top:116px}

/* membership */
.membership{top:2140px;height:800px}
.plan{position:absolute;top:226px;width:275px;height:423px;background:var(--white);box-shadow:0 4px 18px rgba(0,0,0,.12);text-align:center;overflow:hidden}
.plan-head{height:48px;line-height:48px;background:var(--card-darker);color:var(--white);font-family:"Montserrat",sans-serif;font-weight:700;font-size:15px;letter-spacing:1px}
.plan-price{position:relative;height:150px;background:var(--card-dark);clip-path:polygon(0 0,100% 0,100% 66%,50% 100%,0 66%)}
.price{padding-top:18px;font-family:"Montserrat",sans-serif;color:var(--white);font-size:42px;font-weight:400}
.price small{font-size:16px}
.price sup{font-size:20px;vertical-align:14px}
.saving{position:absolute;left:30px;right:30px;top:82px;height:32px;line-height:32px;background:var(--card-darker);color:var(--white);font-family:"Montserrat",sans-serif;font-weight:700;font-size:12px}
.plan ul{list-style:none;margin:18px 24px 0}
.plan li{font-size:11px;line-height:25px;border-bottom:1px solid var(--line);color:var(--text)}
.plan .btn{margin-top:18px;height:28px;font-size:11px}
.plan.featured{top:200px;height:476px}
.plan.featured .plan-head{background:var(--yellow);color:var(--ink);height:60px;line-height:68px}
.plan.featured .plan-price{height:170px;background:var(--pink)}
.plan.featured .price{padding-top:26px}
.plan.featured .saving{background:var(--yellow);color:var(--ink);top:96px}
.plan.featured ul{margin-top:26px}
.ribbon{position:absolute;right:0;top:0}

/* testimonials */
.testimonials{top:2940px;height:556px;background:var(--soft)}
.quote-card{position:absolute;top:204px;width:450px;height:248px;background:var(--white);border-radius:0 60px 0 60px;padding:30px 44px 0 70px}
.stars{color:var(--yellow);font-size:13px;letter-spacing:1px}
.quote-mark{position:absolute;font-family:Georgia,serif;font-size:54px;color:#bdbdbd;line-height:1}
.quote-card p{margin-top:6px;font-size:11px;line-height:18px;color:var(--muted)}
.quote-name{margin-top:14px;font-family:"Montserrat",sans-serif;font-weight:700;font-size:10px;color:var(--pink)}
.quote-place{font-size:9px;color:var(--muted)}
.testimonials .dots{position:absolute;left:993px;top:476px}

/* recipes */
.recipes{top:3496px;height:610px}
.recipes-bg{left:0;top:0;width:711px;height:610px;background:linear-gradient(135deg,#8fa24a,#d9784a 35%,#e8c79d 60%,#6e7f3a)}
.recipes-photo{left:151px;top:124px;width:479px;height:436px;border:8px solid var(--white);box-shadow:0 10px 30px rgba(0,0,0,.3);background:linear-gradient(150deg,#f3f0ea,#7a4a33 40%,#3b2a22 70%,#6a8a3c)}
.recipes .text-block{left:730px;top:144px}

/* gallery */
.gallery{top:4106px;height:560px}
.gallery-item{position:absolute;top:258px;width:215px;height:208px}
.gallery-soup{left:127px;background:linear-gradient(135deg,#e89a2e,#f2c24a 50%,#2a5aa0)}
.gallery-run{left:369px;background:linear-gradient(160deg,#7b8aa0,#c7475a 45%,#3a3f52)}
.gallery-coach{left:610px;background:linear-gradient(150deg,#e9e2dc,#c9b7a8 50%,#7a7270)}
.gallery-platter{left:851px;background:linear-gradient(140deg,#e2d6c2,#7aa84a 45%,#e0622e 75%,#f2efe6)}
.arrow{position:absolute;top:350px}

/* footer */
.site-footer{top:4666px;height:362px;background:var(--soft)}
.site-footer .brand{left:127px;top:62px}
.footer-col{position:absolute;top:60px;font-size:11px;color:var(--text)}
.footer-col h4{font-family:"Montserrat",sans-serif;font-weight:700;font-size:11px;color:var(--pink);margin-bottom:18px;letter-spacing:.5px}
.contact-row{display:flex;gap:12px;align-items:flex-start;margin-bottom:16px;line-height:16px}
.menu-list{list-style:none;line-height:16px}
.social-row{display:flex;align-items:center;gap:12px;margin-bottom:12px;font-family:"Montserrat",sans-serif;font-weight:600;font-size:11px;color:var(--ink)}
.social-row i{display:block;width:24px;height:24px;border-radius:50%;background:var(--pink)}
.footer-rule{left:127px;top:261px;width:946px;height:1px;background:#d8d5d8}
.copyright{left:0;top:310px;width:1200px;text-align:center;font-size:10px;color:var(--muted)}
</style>
</head>
<body>

<header class="section site-header">
  <div class="abs brand">
    <span class="brand-dot"></span>
    <span class="brand-name">Tess Vallory</span>
  </div>
  <div class="abs follow">FOLLOW US <i></i><i></i><i></i></div>
  <div class="abs call">
    <svg width="18" height="18" viewBox="0 0 24 24"><path d="M6.6 10.8a15 15 0 0 0 6.6 6.6l2.2-2.2a1 1 0 0 1 1-.25 11.4 11.4 0 0 0 3.6.57 1 1 0 0 1 1 1V20a1 1 0 0 1-1 1A17 17 0 0 1 3 4a1 1 0 0 1 1-1h3.5a1 1 0 0 1 1 1c0 1.25.2 2.45.57 3.57a1 1 0 0 1-.25 1z" fill="#222"/></svg>
    <div class="call-label">CALL US<b>555.014.2290</b></div>
  </div>
  <nav class="abs main-nav">
    <span class="current">HOME</span><span>BLOG</span><span>ABOUT</span><span>TRAINING PROGRAMS</span><span>HEALTHY FOOD</span><span>SUBSCRIBE</span><span>TESTIMONIALS</span>
  </nav>
</header>

<section class="section hero">
  <div class="hero-copy"><strong>10 week</strong> challenge<br><span class="strong-dark">4 times</span> a year</div>
  <span class="btn">Get Started <svg width="8" height="10" viewBox="0 0 8 10"><path d="M1 1l5 4-5 4" stroke="#fff" stroke-width="2" fill="none"/></svg></span>
  <div class="dots"><i></i><i class="on"></i><i></i><i></i></div>
</section>
<div class="abs hero-photo" role="img" aria-label="Coach helping a smiling client stretch a yellow resistance band while seated on an exercise ball"></div>

<section class="section programs">
  <div class="badge" style="top:132px">Programs</div>
  <div class="program-card" style="left:-316px"><div class="program-photo" role="img" aria-label="Healthy meal photo" style="background:linear-gradient(135deg,#c4752e,#e3a24a)"></div></div>
  <div class="program-card" style="left:67px">
    <div class="program-photo" role="img" aria-label="Plate of salad with boiled eggs, bacon and tomatoes" style="background:linear-gradient(140deg,#6b7a3a,#c8442e 40%,#efe2c8 65%,#7a5a3a)"></div>
    <div class="program-title">HEALTHY FOOD EDUCATION</div>
    <div class="program-desc">Learn to build balanced plates you will enjoy.</div>
    <span class="btn"><svg width="12" height="12" viewBox="0 0 24 24"><path d="M3 4h3l2.5 11h10l2-8H7" stroke="#fff" stroke-width="2.4" fill="none"/><circle cx="10" cy="20" r="1.8" fill="#fff"/><circle cx="17" cy="20" r="1.8" fill="#fff"/></svg>Buy Now</span>
  </div>
  <div class="program-card" style="left:429px">
    <div class="program-photo" role="img" aria-label="Woman doing a handstand on a beach" style="background:linear-gradient(180deg,#9cc6e6,#cfe3ef 50%,#d9c7a3 75%,#b89f74)"></div>
    <div class="program-title">FITNESS TESTING FIRST AND LAST WEEK</div>
    <div class="program-desc">Measure your fitness at the start and finish.</div>
    <span class="btn"><svg width="12" height="12" viewBox="0 0 24 24"><path d="M3 4h3l2.5 11h10l2-8H7" stroke="#fff" stroke-width="2.4" fill="none"/><circle cx="10" cy="20" r="1.8" fill="#fff"/><circle cx="17" cy="20" r="1.8" fill="#fff"/></svg>Buy Now</span>
  </div>
  <div class="program-card" style="left:798px">
    <div class="program-photo" role="img" aria-label="Woman lifting a barbell in a gym" style="background:linear-gradient(150deg,#3d4a5e,#6b6f7a 45%,#8a3c7a 70%,#2c2f38)"></div>
    <div class="program-title">3 WORKOUTS PLUS 1 RUN/WALK PER WEEK</div>
    <div class="program-desc">Short home sessions plus one outdoor session.</div>
    <span class="btn"><svg width="12" height="12" viewBox="0 0 24 24"><path d="M3 4h3l2.5 11h10l2-8H7" stroke="#fff" stroke-width="2.4" fill="none"/><circle cx="10" cy="20" r="1.8" fill="#fff"/><circle cx="17" cy="20" r="1.8" fill="#fff"/></svg>Buy Now</span>
  </div>
  <div class="program-card" style="left:1160px;width:40px;overflow:hidden">
    <div class="program-photo" role="img" aria-label="Workout photo" style="background:linear-gradient(150deg,#e0519a,#b23a7a)"></div>
  </div>
</section>

<section class="section about">
  <div class="abs about-back" role="img" aria-label="Dark background photo of the gym"></div>
  <div class="abs about-photo" role="img" aria-label="Coach and a friend in red aprons smiling in a workshop"></div>
  <div class="text-block">
    <span class="badge">About me</span>
    <h3>On the other hand, we denounce with righteous indignation and dislike men who are so...</h3>
    <p>I am a mum, a coach and a firm believer that small daily habits build lasting change. My approach is simple: commit to your training, work hard consistently and the results follow. Every challenge is built to fit around real family life.</p>
    <span class="btn">Read More</span>
  </div>
</section>

<section class="section membership">
  <div class="badge" style="top:74px">Membership</div>

  <div class="plan" style="left:134px">
    <div class="plan-head">MONTHLY</div>
    <div class="plan-price"><div class="price"><sup>$</sup>24.95<small>/mo</small></div><div class="saving">NO SAVINGS</div></div>
    <ul><li>Full 10 week program</li><li>Weekly workout plans</li><li>Meal guide and recipes</li><li>Private member group</li><li>Progress check-ins</li></ul>
    <span class="btn">Get Started <svg width="7" height="9" viewBox="0 0 8 10"><path d="M1 1l5 4-5 4" stroke="#fff" stroke-width="2" fill="none"/></svg></span>
  </div>

  <div class="plan featured" style="left:463px">
    <div class="plan-head">YEARLY</div>
    <div class="plan-price"><div class="price"><sup>$</sup>19.95<small>/mo</small></div><div class="saving">SAVE $60.00/YEAR</div></div>
    <ul><li>Full 10 week program</li><li>Weekly workout plans</li><li>Meal guide and recipes</li><li>Private member group</li><li>Progress check-ins</li></ul>
    <span class="btn">Get Started <svg width="7" height="9" viewBox="0 0 8 10"><path d="M1 1l5 4-5 4" stroke="#fff" stroke-width="2" fill="none"/></svg></span>
    <svg class="ribbon" width="80" height="80" viewBox="0 0 80 80"><path d="M18 0h26l36 36v26z" fill="#5cb85c"/><text x="49" y="31" transform="rotate(45 49 31)" text-anchor="middle" font-family="Montserrat, sans-serif" font-size="8" font-weight="700" fill="#fff">MOST POPULAR</text></svg>
  </div>

  <div class="plan" style="left:794px">
    <div class="plan-head">QUARTERLY</div>
    <div class="plan-price"><div class="price"><sup>$</sup>22.95<small>/mo</small></div><div class="saving">SAVE $14.00/YEAR</div></div>
    <ul><li>Full 10 week program</li><li>Weekly workout plans</li><li>Meal guide and recipes</li><li>Private member group</li><li>Progress check-ins</li></ul>
    <span class="btn">Get Started <svg width="7" height="9" viewBox="0 0 8 10"><path d="M1 1l5 4-5 4" stroke="#fff" stroke-width="2" fill="none"/></svg></span>
  </div>
</section>

<section class="section testimonials">
  <div class="badge" style="top:72px">Testimonials</div>
  <div class="quote-card" style="left:134px">
    <span class="quote-mark" style="left:28px;top:44px">&ldquo;</span>
    <div class="stars">★★★★★</div>
    <p>Joining this challenge was the best decision I made this year. The workouts fit around my kids, the recipes are easy and the support kept me going on the hard days. I feel stronger and more confident than ever.</p>
    <span class="quote-mark" style="right:48px;top:150px">&rdquo;</span>
    <div class="quote-name">MARLOWE</div><div class="quote-place">England</div>
  </div>
  <div class="quote-card" style="left:620px">
    <span class="quote-mark" style="left:28px;top:44px">&ldquo;</span>
    <div class="stars">★★★★★</div>
    <p>Ten weeks ago I could barely run to the corner. Now I walk and run three times a week, I cook real food for my family and I have lost the weight I carried for years. Thank you Tess.</p>
    <span class="quote-mark" style="right:48px;top:150px">&rdquo;</span>
    <div class="quote-name">MARLOWE</div><div class="quote-place">England</div>
  </div>
  <div class="dots"><i class="on"></i><i></i><i></i><i></i><i></i></div>
</section>

<section class="section recipes">
  <div class="abs recipes-bg" role="img" aria-label="Close-up of salmon and fresh salad greens"></div>
  <div class="abs recipes-photo" role="img" aria-label="Chocolate smoothie in a glass beside an avocado half and dates"></div>
  <div class="text-block">
    <span class="badge">Recipes</span>
    <h3>On the other hand, we denounce with righteous indignation and dislike.</h3>
    <p>Every member gets a growing library of quick, family friendly recipes. Each one lists simple ingredients, clear steps and the nutrition you need, so healthy eating becomes part of your routine rather than another chore on the list.</p>
    <span class="btn">Read More</span>
  </div>
</section>

<section class="section gallery">
  <div class="badge" style="top:120px">Gallery</div>
  <svg class="arrow" style="left:76px" width="14" height="20" viewBox="0 0 14 20"><path d="M11 2L3 10l8 8" stroke="#444" stroke-width="2.5" fill="none"/></svg>
  <div class="gallery-item gallery-soup" role="img" aria-label="Bowl of pumpkin soup"></div>
  <div class="gallery-item gallery-run" role="img" aria-label="Group of women after a fun run"></div>
  <div class="gallery-item gallery-coach" role="img" aria-label="Coach smiling after a workout"></div>
  <div class="gallery-item gallery-platter" role="img" aria-label="Platter of dip with fresh vegetables"></div>
  <svg class="arrow" style="left:1104px" width="14" height="20" viewBox="0 0 14 20"><path d="M3 2l8 8-8 8" stroke="#444" stroke-width="2.5" fill="none"/></svg>
</section>

<footer class="section site-footer">
  <div class="abs brand">
    <span class="brand-dot"></span>
    <span class="brand-name">Tess Vallory</span>
  </div>
  <div class="footer-col" style="left:496px">
    <h4>CONTACT US</h4>
    <div class="contact-row"><svg width="12" height="14" viewBox="0 0 24 28"><path d="M12 1a9 9 0 0 0-9 9c0 7 9 17 9 17s9-10 9-17a9 9 0 0 0-9-9zm0 12a3 3 0 1 1 0-6 3 3 0 0 1 0 6z" fill="#555"/></svg><span>17 Orchard Lane<br>Millbrook, OR 97001</span></div>
    <div class="contact-row"><svg width="12" height="12" viewBox="0 0 24 24"><path d="M6.6 10.8a15 15 0 0 0 6.6 6.6l2.2-2.2a1 1 0 0 1 1-.25 11.4 11.4 0 0 0 3.6.57 1 1 0 0 1 1 1V20a1 1 0 0 1-1 1A17 17 0 0 1 3 4a1 1 0 0 1 1-1h3.5a1 1 0 0 1 1 1c0 1.25.2 2.45.57 3.57a1 1 0 0 1-.25 1z" fill="#555"/></svg><span>555.014.2290</span></div>
    <div class="contact-row"><svg width="13" height="10" viewBox="0 0 26 20"><rect x="1" y="1" width="24" height="18" rx="2" fill="none" stroke="#555" stroke-width="2"/><path d="M1 2l12 9 12-9" fill="none" stroke="#555" stroke-width="2"/></svg><span>hello@tessvallory.com</span></div>
  </div>
  <div class="footer-col" style="left:730px">
    <h4>MENU</h4>
    <ul class="menu-list"><li>Home</li><li>Blog</li><li>About</li><li>Training programs</li><li>Healthy food</li><li>Subscribe</li><li>Testimonials</li></ul>
  </div>
  <div class="footer-col" style="left:938px">
    <h4>CONNECT WITH US</h4>
    <div class="social-row"><i></i>PALSHARE</div>
    <div class="social-row"><i></i>SNAPLORIA</div>
    <div class="social-row"><i></i>VID HOLLOW</div>
  </div>
  <div class="abs footer-rule"></div>
  <div class="abs copyright">Copyright @ 2018 All Rights Reserved</div>
</footer>

</body>
</html>
```